Belle Rive Weddings and Events

I am a small boutique wedding coordinator, stylist and bridal consultant/coach/assistant. I am based in Brisbane, Australia and my business is geared towards mid range- high end budget bridal couples.
I am after some business cards that are double sided, with the logo on one side and all other information on the other side, including the business tagline of design, create, celebrate. The look of the card needs to be clean and crisp, with white and the tones of grey of the logo.The final design needs to convey sophistication and poise. Perhaps the logo and tagline could be done in a metallic silver with the rest of the text in the shades of grey from the style guide attached below.
Title- Mira Tolvarenko - Director / Events Manager and Stylist
Address - 218 Halbrook Terrace, Wexley Vale, QLD, 4127
Phone- 07 3894 2167
Mobile- 0438 725 519
Email- Mira@bellerivecelebra.com.au
Website- www.bellerivecelebra.com.au

```html
<!DOCTYPE html>
<html lang="en">
<head>
<meta charset="utf-8">
<title>Belle Rive Weddings and Events – Business Card</title>
<link rel="stylesheet" href="https://fonts.googleapis.com/css2?family=Questrial&family=Montserrat:wght@600&display=swap">
<style>
  :root {
    --backdrop: #e6e6e6;
    --card-dark: #1d1d1d;
    --card-dark-edge: #2a2a2a;
    --card-light: #fbfbfb;
    --silver: #9d9d9d;
    --silver-soft: #bdbdbd;
    --ink: #1f1f1f;
    --ink-soft: #3a3a3a;
    --flourish: #d9d9d9;
  }
  * { box-sizing: border-box; margin: 0; padding: 0; }
  html, body {
    width: 1200px;
    height: 720px;
    overflow: hidden;
    background: var(--backdrop);
  }
  .canvas {
    position: relative;
    width: 1200px;
    height: 720px;
  }
  .card {
    position: absolute;
    top: 241px;
    width: 420px;
    height: 240px;
    font-family: "Questrial", sans-serif;
    text-align: center;
  }
  .card-front {
    left: 147px;
    background: linear-gradient(135deg, var(--card-dark-edge), var(--card-dark));
  }
  .card-back {
    left: 633px;
    background: var(--card-light);
    color: var(--ink);
  }
  .brand {
    position: absolute;
    left: 0;
    right: 0;
    top: 86px;
    display: flex;
    align-items: center;
    justify-content: center;
    gap: 10px;
    color: var(--silver);
    font-size: 17px;
    letter-spacing: 0.5px;
  }
  .brand-dot {
    width: 8px;
    height: 8px;
    border-radius: 50%;
    background: var(--silver);
  }
  .front-tagline {
    position: absolute;
    left: 0;
    right: 0;
    top: 201px;
    color: var(--silver-soft);
    font-size: 10.5px;
    letter-spacing: 0.2px;
  }
  .flourish {
    position: absolute;
    left: 134px;
    top: 24px;
    width: 152px;
    height: 26px;
    background: var(--flourish);
    border-radius: 13px;
  }
  .holder-name {
    position: absolute;
    left: 0;
    right: 0;
    top: 56px;
    font-family: "Montserrat", sans-serif;
    font-weight: 600;
    font-size: 18px;
    color: var(--ink);
  }
  .holder-title {
    position: absolute;
    left: 0;
    right: 0;
    top: 80px;
    font-size: 9.5px;
    color: var(--ink-soft);
  }
  .contact-line {
    position: absolute;
    left: 0;
    right: 0;
    font-size: 12px;
    color: var(--ink);
  }
  .phone { top: 105px; }
  .mobile { top: 120px; }
  .email { top: 145px; }
  .address { top: 170px; }
  .website { top: 209px; color: var(--ink-soft); }
  .website strong { font-weight: 400; color: var(--ink); }
</style>
</head>
<body>
<main class="canvas">
  <section class="card card-front" aria-label="Card front">
    <div class="brand">
      <span class="brand-dot"></span>
      <span class="brand-name">Belle Rive Weddings and Events</span>
    </div>
    <p class="front-tagline">Wedding Coordinator, Stylist and Bridal Consultant/Coach/Assistant</p>
  </section>

  <section class="card card-back" aria-label="Card back">
    <div class="flourish" role="img" aria-label="Decorative scroll flourish"></div>
    <h1 class="holder-name">Mira Tolvarenko</h1>
    <p class="holder-title">Director / Events Manager and Stylist</p>
    <p class="contact-line phone">Phone: 07 3894 2167</p>
    <p class="contact-line mobile">Mobile: 0438 725 519</p>
    <p class="contact-line email">Email: Mira@bellerivecelebra.com.au</p>
    <p class="contact-line address">218 Halbrook Terrace, Wexley Vale, QLD, 4127</p>
    <p class="contact-line website">www.<strong>bellerivecelebra</strong>.com.au</p>
  </section>
</main>
</body>
</html>
```